Medical Learning Web Design Project

The web site will be a site for medical students. It is aimed at providing a collaborative place for students to study, learn, question each other and challenge each other with learning. The site needs to have a section on the page that is for the content and this needs to be relatively clean and clinical. The surrounding elements will be informative (for the statistics, challenge etc). There will also be a slide-out screen that allows for the social/friend elements of the site.

The colour scheme needs to be clean and clinical where appropriate, but also engaging and exciting for the social/competitive elements.
Updates

Just for clarity: The site isn't expected to be 'coded' ... it is just the layered PSD files that I need.

Also, with regards to the navigation buttons ... they will never ALL be present at the same time so don't feel the need to design all on one page, but creativity around allowing few or many on a page will be an advantage ...

Thanks

Hi,

Please note that the image uploaded has been done as a wireframe by the developers. I am looking for a more creative and engaging way of presenting that content ...

Thanks

Hi all

Thank you all for the designs so far ...!

Please have a look at the new uploaded file, I am also looking not just for a 'templated home page' but also some different layouts that are represented in these wireframes. If the various layouts represented can be condensed down into 1 or 2 page templates with appropriate colour schemes to capture the type of content on the page (as already mentioned ... social .. competitive ... learning), then that will help me live the concepts better too! The friends tab for instance I have envisaged as a slider covering the screen and then sliding back when complete ... but let me see what creativity you can give to this ...!

Many thanks

Target Market(s)

Medical Students

Industry/Entity Type

Medical

Requirements
Must have
• - Not cluttered appearance
- Dynamic navigation (ie. site will be developed to only show relevant navigation buttons on each page ...)
- Navigation buttons (need to be individual buttons) will be: 'Home', 'Take the tour', 'What your peers say', 'Subscriptions', 'Free Signup', 'Contact us', 'Moderation', 'Statistics', 'Competition', 'Answer Questions', 'Post Questions', 'My profile', 'Friends'
- Please also ensure it is engaging for social elements and competitive elements (perhaps slightly different design for pages focussed on each element)
- Please also ensure that there is a masculine design and feminine design that has continuity for the site but depending on gender the design can be tailored to be more appealing (that means perhaps male social design, male competitive design, female social design, female competitive design ... without loosing continuity through the site).
- Photoshop PSD format
- Pixel perfect at least 1000 pixels wide (but the design needs to allow for various monitor sizes (only desktop or laptops ... not tablets or smart phones)

```html
<!DOCTYPE html>
<html lang="en">
<head>
<meta charset="utf-8">
<title>Medora – The Medical Peer Review</title>
<link rel="stylesheet" href="https://fonts.googleapis.com/css2?family=Arimo:ital,wght@0,400;0,700;1,400;1,700&display=swap">
<style>
:root{
  --red:#e8141b;
  --red-dark:#b3161c;
  --red-deep:#8f1015;
  --ink:#333;
  --muted:#666;
  --line:#c9c9c9;
  --panel:#e6e6e6;
  --white:#fff;
}
*{box-sizing:border-box;margin:0;padding:0}
html,body{width:1200px;height:1080px;overflow:hidden;background:var(--white);font-family:"Arimo",Arial,sans-serif;color:var(--ink)}
.page{position:relative;width:1200px;height:1080px}
.top-band{position:absolute;left:0;top:0;width:1200px;height:12px;background:var(--red-dark)}

.brand{position:absolute;left:97px;top:64px;display:flex;align-items:center;gap:14px}
.brand-mark{width:84px;height:84px;border-radius:50%;background:var(--red)}
.brand-name{font-size:52px;font-weight:400;color:var(--muted);line-height:1}
.brand-tag{font-size:16px;color:var(--muted);margin-top:3px;white-space:nowrap}

.quote{position:absolute;left:408px;top:121px;width:390px;font-size:11px;font-style:italic;color:var(--muted);text-align:right;line-height:1.35}
.quote-line{text-align:left}
.stats-call{position:absolute;left:505px;top:155px;font-size:16px;font-weight:700;font-style:italic;color:#777}

.social{position:absolute;left:706px;top:40px;display:flex;align-items:center;gap:7px;font-size:11px;color:#555}
.social-label{margin-right:6px}
.social-icon{width:20px;height:20px;border-radius:3px;background:#6b7fa8}
.social-icon.green{background:#5aa33a}.social-icon.sky{background:#4a9ad8}.social-icon.orange{background:#e6812a}.social-icon.grey{background:#8a8a8a}

.login{position:absolute;left:862px;top:84px;width:186px;font-size:15px;color:#444}
.login label{display:block;line-height:18px}
.login .field{display:block;width:186px;height:24px;border:1px solid #aaa;background:var(--white);margin:2px 0 5px}
.forgot{font-size:8px;color:#555;text-decoration:underline;line-height:10px;margin-top:-3px}
.login-row{display:flex;justify-content:space-between;align-items:center;margin-top:-8px;font-size:10px;height:24px}
.keep{display:flex;align-items:center;gap:4px;margin-top:14px}
.keep i{width:8px;height:8px;border:1px solid #999;display:inline-block}
.login-btn{width:75px;height:23px;border:1px solid #aaa;border-radius:5px;background:linear-gradient(#fafafa,#ddd);font-size:12px;display:flex;align-items:center;justify-content:center}

.nav{position:absolute;left:96px;top:220px;width:986px;height:47px;border-radius:30px 30px 0 0;background:linear-gradient(#d21f25,var(--red-deep));display:flex;align-items:center;justify-content:center}
.nav a{color:var(--white);text-decoration:none;font-size:16px;padding:0 30px;position:relative;white-space:nowrap}
.nav a+a::before{content:"";position:absolute;left:0;top:2px;height:16px;border-left:1px solid rgba(255,255,255,.6)}
.rule{position:absolute;left:0;top:267px;width:1200px;height:2px;background:var(--line)}

.hero{position:absolute;left:96px;top:269px;width:986px;height:411px;border-radius:0 0 28px 28px;background:linear-gradient(100deg,#dfe3e6 0%,#f4f5f4 45%,#e9ece8 70%,#cfd6d3 100%)}
.dots{position:absolute;left:560px;top:655px;display:flex;gap:9px}
.dots i{width:9px;height:9px;border-radius:50%;background:rgba(255,255,255,.8)}
.arrow{position:absolute;top:432px}

.card{position:absolute;top:695px;height:288px;border:2px dotted var(--line);border-radius:6px;background:var(--white)}
.works{left:97px;width:390px;padding:14px 16px}
.works h2{font-size:24px;font-weight:400;color:#777}
.works h2 b{color:#666}
.video{margin-top:12px;width:356px;height:220px;background:#000;position:relative}
.video-bar{position:absolute;left:0;bottom:0;width:100%;height:18px;background:#222;display:flex;align-items:center;gap:8px;padding:0 8px;font-size:8px;color:#ccc}
.video-bar .track{flex:1;height:3px;background:#555}
.spinner{position:absolute;left:170px;top:95px}

.news{position:absolute;left:510px;top:700px;width:372px;height:283px;background:var(--panel);border-radius:0 0 10px 10px}
.news-head{position:absolute;left:-9px;top:-10px;width:381px;height:48px;background:var(--red);border-radius:14px 14px 0 0;color:var(--white);padding:6px 12px 0 60px;line-height:1.1}
.news-head .dot{position:absolute;left:14px;top:8px;width:32px;height:32px;border-radius:50%;background:var(--white)}
.news-head small{display:block;font-size:12px;font-weight:700}
.news-head strong{font-size:16px}
.news-list{position:absolute;left:12px;top:44px;width:350px;list-style:none}
.news-list li{padding:6px 10px 5px 24px;border-bottom:1px solid var(--white);font-size:12.5px;line-height:1.3;color:#555}
.news-list li:last-child{border-bottom:0}
.news-list li span{display:block;font-size:9px;line-height:11px;color:#222;margin-top:4px}

.circle{left:897px;width:185px;padding:10px 12px;font-size:10px;color:#444}
.circle-top{display:flex;gap:8px}
.circle-top .dot{width:40px;height:40px;border-radius:50%;background:var(--red)}
.circle-top b{color:#3b5998;font-size:12px}
.like{display:inline-flex;align-items:center;height:16px;padding:0 6px;border:1px solid #999;background:#eee;font-size:9px;margin-top:6px}
.like-note{font-size:9px;margin-left:6px}
.count{margin:14px 0 16px;font-size:9px}
.people{display:grid;grid-template-columns:repeat(3,45px);gap:4px 6px;justify-content:center}
.person{text-align:center;font-size:8px;color:#666}
.person svg{display:block;margin-bottom:4px}
.plugin{border-top:1px solid #ddd;margin-top:14px;padding-top:6px;font-size:8px;display:flex;align-items:center;gap:5px}
.plugin i{width:10px;height:10px;background:#3b5998;display:inline-block}

.footer{position:absolute;left:0;top:1000px;width:1200px;height:80px;background:var(--red);color:var(--white)}
.footer-nav{position:absolute;top:13px;left:0;width:1200px;display:flex;justify-content:center;font-size:11px}
.footer-nav a{color:var(--white);text-decoration:none;padding:0 33px;position:relative;white-space:nowrap}
.footer-nav a+a::before{content:"|";position:absolute;left:0}
.copyright{position:absolute;top:45px;width:1200px;text-align:center;font-size:11px}
</style>
</head>
<body>
<div class="page">
  <div class="top-band"></div>

  <header>
    <div class="brand">
      <div class="brand-mark"></div>
      <div>
        <div class="brand-name">Medora</div>
        <div class="brand-tag">The Medical Peer Review</div>
      </div>
    </div>

    <blockquote class="quote">
      <p class="quote-line">"Medora keeps me ahead of the game, constantly testing my knowledge..."</p>
      <p>--Ravi, doctor in training, Northfield University</p>
    </blockquote>
    <p class="stats-call">How will your stats compare?</p>

    <div class="social">
      <span class="social-label">Medora on the web</span>
      <i class="social-icon"></i><i class="social-icon sky"></i><i class="social-icon"></i><i class="social-icon"></i><i class="social-icon grey"></i><i class="social-icon green"></i><i class="social-icon sky"></i><i class="social-icon"></i><i class="social-icon orange"></i>
    </div>

    <form class="login">
      <label>Username:<span class="field"></span></label>
      <label>Password:<span class="field"></span></label>
      <div class="forgot">Forgot your password?</div>
      <div class="login-row">
        <span class="keep"><i></i>Keep me signed in</span>
        <span class="login-btn">Login</span>
      </div>
    </form>
  </header>

  <nav class="nav">
    <a href="#">Home</a><a href="#">Take The Tour</a><a href="#">What Your Peers Say</a><a href="#">Subscription Plans</a><a href="#">Free Sign Up</a><a href="#">Contact Us</a>
  </nav>
  <div class="rule"></div>

  <svg class="arrow" style="left:57px" width="26" height="42" viewBox="0 0 26 42"><path d="M26 0 L0 21 L26 42 Z" fill="#d4d4d4"/></svg>
  <div class="hero" role="img" aria-label="Photo of a senior doctor demonstrating an anatomy model to a group of medical students in a bright classroom"></div>
  <div class="dots"><i></i><i></i><i></i><i></i><i></i></div>
  <svg class="arrow" style="left:1092px" width="26" height="42" viewBox="0 0 26 42"><path d="M0 0 L26 21 L0 42 Z" fill="#d4d4d4"/></svg>

  <section class="card works">
    <h2>How Medora <b>Works</b></h2>
    <div class="video">
      <svg class="spinner" width="18" height="18" viewBox="0 0 18 18"><circle cx="9" cy="9" r="6" fill="none" stroke="#bbb" stroke-width="3" stroke-dasharray="3 3"/></svg>
      <div class="video-bar"><span>▮▮</span><span>0:00 / 2:20</span><span class="track"></span><span>▭ ▢</span></div>
    </div>
  </section>

  <section class="news">
    <div class="news-head"><span class="dot"></span><small>The Medical Peer Review</small><strong>Medora</strong></div>
    <ul class="news-list">
      <li>Lorem ipsum dolor sit amet, consectetuer adipisc-ing elit, sed diam nonummy nibh euismod tincidunt<span>02.4/2013</span></li>
      <li>Lorem ipsum dolor sit amet, consectetuer adipisc-ing elit, sed diam nonummy nibh euismod tincidunt<span>02.4/2013</span></li>
      <li>Lorem ipsum dolor sit amet, consectetuer adipisc-ing elit, sed diam nonummy nibh euismod tincidunt<span>02.4/2013</span></li>
      <li>Lorem ipsum dolor sit amet, consectetuer adipisc-ing elit, sed diam nonummy nibh euismod tincidunt<span>02.4/2013</span></li>
    </ul>
  </section>

  <aside class="card circle">
    <div class="circle-top">
      <span class="dot"></span>
      <div><b>Medora</b> on Circle<br><span class="like">Like</span><span class="like-note">You like this.</span></div>
    </div>
    <p class="count">22,407 people like <b>Medora</b></p>
    <div class="people">
      <div class="person"><svg width="45" height="45"><rect x=".5" y=".5" width="44" height="44" fill="#fff" stroke="#555"/><path d="M0 0L45 45M45 0L0 45" stroke="#555"/></svg>Person</div>
      <div class="person"><svg width="45" height="45"><rect x=".5" y=".5" width="44" height="44" fill="#fff" stroke="#555"/><path d="M0 0L45 45M45 0L0 45" stroke="#555"/></svg>Person</div>
      <div class="person"><svg width="45" height="45"><rect x=".5" y=".5" width="44" height="44" fill="#fff" stroke="#555"/><path d="M0 0L45 45M45 0L0 45" stroke="#555"/></svg>Person</div>
      <div class="person"><svg width="45" height="45"><rect x=".5" y=".5" width="44" height="44" fill="#fff" stroke="#555"/><path d="M0 0L45 45M45 0L0 45" stroke="#555"/></svg>Person</div>
      <div class="person"><svg width="45" height="45"><rect x=".5" y=".5" width="44" height="44" fill="#fff" stroke="#555"/><path d="M0 0L45 45M45 0L0 45" stroke="#555"/></svg>Person</div>
      <div class="person"><svg width="45" height="45"><rect x=".5" y=".5" width="44" height="44" fill="#fff" stroke="#555"/><path d="M0 0L45 45M45 0L0 45" stroke="#555"/></svg>Person</div>
    </div>
    <div class="plugin"><i></i>Circle social plugin</div>
  </aside>

  <footer class="footer">
    <nav class="footer-nav">
      <a href="#">Home</a><a href="#">Take The Tour</a><a href="#">What Your Peers Say</a><a href="#">Subscription Plans</a><a href="#">Free Signup</a><a href="#">Contact Us</a><a href="#">Site Map</a>
    </nav>
    <p class="copyright">Copyright 2012 Medora Limited</p>
  </footer>
</div>
</body>
</html>
```